Banner Ad Design for Resume Builder Needed

For the ad copy and design of the ad, I leave that up to you. Keep in mind this is a do-it-yourself online resume builder. The site is simple to use and geared towards people who are unsure of how to write/create their own resume.

You can view the site (which isn't finished) and how it works at http://cvcrafter.demo.tplwerks.net/

I do not want the same color scheme or the logo used in the ad, just the most appealing ad for those looking to use a product like this

I need the ad in these sizes:

300x250, 728x90, 160x600, 468x60, 120x600, 300x100

```html
<!DOCTYPE html>
<html lang="en">
<head>
<meta charset="utf-8">
<title>Brightfolio Banner Set</title>
<link rel="stylesheet" href="https://fonts.googleapis.com/css2?family=Lato:wght@300;400;700;900&display=swap">
<style>
:root{
  --stage:#737172;
  --panel:#262626;
  --white:#ffffff;
  --brand:#262626;
  --cta:#fff52e;
  --cta-text:#3a3a3a;
}
*{margin:0;padding:0;box-sizing:border-box}
html,body{width:1200px;height:1000px;overflow:hidden}
body{background:var(--stage);position:relative;font-family:'Lato',sans-serif}
.banner{position:absolute;background:var(--panel);overflow:hidden}
.logo-band{position:absolute;background:var(--white)}
.brand{position:absolute;display:flex;align-items:center;gap:6px;white-space:nowrap}
.brand-square{background:var(--brand);display:block}
.brand-name{color:var(--brand);font-weight:700;font-family:'Lato',sans-serif}
.pointer{position:absolute;width:0;height:0}
.pointer-down{border-left:12px solid transparent;border-right:12px solid transparent;border-top:12px solid var(--white)}
.pointer-right{border-top:9px solid transparent;border-bottom:9px solid transparent;border-left:9px solid var(--white)}
.headline{position:absolute;color:var(--white);font-weight:900;text-transform:uppercase;line-height:.98;text-shadow:2px 2px 4px rgba(0,0,0,.8)}
.subline{position:absolute;color:var(--white);font-weight:300;text-transform:uppercase;line-height:1.05}
.cta{position:absolute;background:var(--cta);color:var(--cta-text);font-weight:700;border-radius:6px;display:flex;align-items:center;justify-content:center;font-family:'Lato',sans-serif}
.photo{position:absolute;display:block}

/* 160x600 */
.sky-wide{left:175px;top:100px;width:160px;height:600px}
.sky-wide .logo-band{left:0;top:0;width:160px;height:90px}
/* 152x600 */
.sky-narrow{left:355px;top:100px;width:152px;height:600px}
.sky-narrow .logo-band{left:0;top:0;width:152px;height:90px}
.sky .brand{top:34px;left:10px}
.sky .brand-square{width:18px;height:18px}
.sky .brand-name{font-size:19px}
.sky .pointer{top:90px}
.sky .headline{left:15px;top:128px;font-size:29px}
.sky .subline{top:221px;font-size:18px;text-align:center;width:100%}
.sky .cta{top:290px;height:31px;font-size:13px}
.sky .photo{left:0;top:370px;height:230px}

/* 336x280 */
.rect{left:530px;top:420px;width:336px;height:280px}
.rect .logo-band{left:0;top:0;width:210px;height:58px}
.rect .brand{left:12px;top:16px}
.rect .brand-square{width:24px;height:24px}
.rect .brand-name{font-size:24px}
.rect .pointer{left:83px;top:58px}
.rect .headline{left:33px;top:73px;font-size:30px}
.rect .subline{left:30px;top:166px;width:135px;text-align:center;font-size:18px}
.rect .cta{left:3px;top:228px;width:168px;height:36px;font-size:14px;border-radius:8px}
.rect .photo{left:170px;top:0;width:166px;height:280px}

/* 468x58 */
.leader-small{left:174px;top:728px;width:468px;height:58px}
.leader-small .logo-band{left:0;top:0;width:132px;height:58px}
.leader-small .brand{left:20px;top:11px;gap:4px}
.leader-small .brand-square{width:12px;height:12px}
.leader-small .brand-name{font-size:14px}
.leader-small .cta{left:16px;top:35px;width:96px;height:20px;font-size:8px;border-radius:4px}
.leader-small .pointer{left:132px;top:20px;border-top-width:7px;border-bottom-width:7px;border-left-width:7px}
.leader-small .headline{left:132px;width:200px;top:5px;font-size:19px;text-align:center;line-height:.95}
.leader-small .subline{left:132px;width:204px;top:43px;font-size:11px;text-align:center;font-weight:400}
.leader-small .photo{left:350px;top:0;width:118px;height:58px}

/* 728x90 */
.leader-large{left:174px;top:813px;width:728px;height:90px}
.leader-large .logo-band{left:0;top:0;width:206px;height:90px}
.leader-large .brand{left:34px;top:19px}
.leader-large .brand-square{width:18px;height:18px}
.leader-large .brand-name{font-size:21px}
.leader-large .cta{left:28px;top:55px;width:147px;height:30px;font-size:13px}
.leader-large .pointer{left:206px;top:36px}
.leader-large .headline{left:206px;width:300px;top:7px;font-size:31px;text-align:center;line-height:.97}
.leader-large .subline{left:204px;width:300px;top:66px;font-size:18px;text-align:center}
.leader-large .photo{left:545px;top:0;width:183px;height:90px}
</style>
</head>
<body>

<svg width="0" height="0" style="position:absolute">
  <defs>
    <linearGradient id="office-tones" x1="0" y1="0" x2="1" y2="1">
      <stop offset="0" stop-color="#eef0f3"/>
      <stop offset=".5" stop-color="#b9bcc2"/>
      <stop offset="1" stop-color="#8a8d95"/>
    </linearGradient>
  </defs>
</svg>

<section class="banner sky sky-wide">
  <div class="logo-band">
    <div class="brand"><span class="brand-square"></span><span class="brand-name">Brightfolio</span></div>
  </div>
  <div class="pointer pointer-down" style="left:68px"></div>
  <h2 class="headline">Online<br>Resume<br>Builder</h2>
  <p class="subline">Create their<br>own resume</p>
  <a class="cta" style="left:9px;width:146px">Build A Resume</a>
  <svg class="photo" width="160" height="230" viewBox="0 0 160 230" role="img" aria-label="Photo of smiling business people seated at a desk">
    <path d="M0 40 Q40 0 110 0 Q145 2 160 12 V230 H0 Z" fill="url(#office-tones)"/>
  </svg>
</section>

<section class="banner sky sky-narrow">
  <div class="logo-band">
    <div class="brand" style="left:8px"><span class="brand-square"></span><span class="brand-name">Brightfolio</span></div>
  </div>
  <div class="pointer pointer-down" style="left:64px"></div>
  <h2 class="headline" style="left:14px">Online<br>Resume<br>Builder</h2>
  <p class="subline">Create their<br>own resume</p>
  <a class="cta" style="left:8px;width:139px">Build A Resume</a>
  <svg class="photo" width="152" height="230" viewBox="0 0 152 230" role="img" aria-label="Photo of smiling business people seated at a desk">
    <path d="M0 40 Q38 0 105 0 Q140 2 152 12 V230 H0 Z" fill="url(#office-tones)"/>
  </svg>
</section>

<section class="banner rect">
  <div class="logo-band">
    <div class="brand"><span class="brand-square"></span><span class="brand-name">Brightfolio</span></div>
  </div>
  <div class="pointer pointer-down"></div>
  <h2 class="headline">Online<br>Resume<br>Builder</h2>
  <p class="subline">Create their<br>own resume</p>
  <a class="cta">Build A Resume</a>
  <svg class="photo" viewBox="0 0 166 280" role="img" aria-label="Photo of smiling business people seated at a desk">
    <path d="M40 0 Q0 130 25 280 H166 V0 Z" fill="url(#office-tones)"/>
  </svg>
</section>

<section class="banner leader-small">
  <div class="logo-band">
    <div class="brand"><span class="brand-square"></span><span class="brand-name">Brightfolio</span></div>
    <a class="cta">Build A Resume</a>
  </div>
  <div class="pointer pointer-right"></div>
  <h2 class="headline">Online Resume<br>Builder</h2>
  <p class="subline">Create their own resume</p>
  <svg class="photo" viewBox="0 0 118 58" role="img" aria-label="Photo of smiling business people seated at a desk">
    <path d="M8 0 Q-4 30 6 58 H118 V0 Z" fill="url(#office-tones)"/>
  </svg>
</section>

<section class="banner leader-large">
  <div class="logo-band">
    <div class="brand"><span class="brand-square"></span><span class="brand-name">Brightfolio</span></div>
    <a class="cta">Build A Resume</a>
  </div>
  <div class="pointer pointer-right"></div>
  <h2 class="headline">Online Resume<br>Builder</h2>
  <p class="subline">Create their own resume</p>
  <svg class="photo" viewBox="0 0 183 90" role="img" aria-label="Photo of smiling business people seated at a desk">
    <path d="M12 0 Q-4 45 8 90 H183 V0 Z" fill="url(#office-tones)"/>
  </svg>
</section>

</body>
</html>
```